Brightwell Capital - fund management and algorithmic design

We're looking for a web design for a new company called brightwell capital which is based out of London.

The photography provided will be a major part of the creative content. The intent is to have a sharp, clear, professional, slick look. Less is more and clutter is not the root that should be followed.

A logo has been selected and the photography provided will give the designer a good idea of what we are looking for. The logo designer is still getting back to me with the very final version but what is provided is good enough to move forward with. the final design will likely have this changed slightly.

The photos are about 1.2 meg each at 86 pdi. I believe this is about right for a high quality web image.

At some point on the site it should have: Integrity, Innovative, Progressive. These are core principles of the company. Also ,Fund management and algorithmic design could be used somewhere as this explains exactly what we do.

I also wish to have the secondary pages designed too. However, rather than asking everybody to do this i will ask a select few designers to look at one of the pages. The chosen designer will then be asked to finish the other pages too. These are expected to be quite simple, nothing fussy - clean and presentable with a small amount of room for artistic license.

Also the links to these two sites will give you a very good idea of what we're looking for.

quendor.com
tavelpointrix.com
birchwardlanefx.com
Updates

Hi,

sorry for as i had problem getting the final images from the photographer as he's been away and busy.

However, we now the the logo (be it not the very final version) and the photos uploaded.  Please read the brief again as this has been updated too.

Initially i'd be happy if you made up the front page and after that i will ask a small handful of designers to submit a design for the secondary page - this way i feel is better as it uses less of your time.  These pages are likely to use the photography for a backdrop too.

Looking forward to your designs.

Regards,

Dominic

Reason: I have extended the deadline as the first week has been held up because of delays in content. thanks, Dominic

Target Market(s)

wealth individuals who wish to diversify their investment portfolios with investments predominantly in the foreign exchange markets as well as some financial products offered by ZPLHoldings.com

Industry/Entity Type

It Company

Requirements
Must have
• There are three photos that the site must use, once the final design is fully operational and coded we want the first three photos to rotate on the front page. Much like quendorr.com

An area where a prospective client can enter their email address to receive market new letters and correspondences from brightwell capital.

front page

about us,
managed accounts
systems and performance

```html
<!DOCTYPE html>
<html lang="en">
<head>
<meta charset="utf-8">
<title>Brightwell Capital</title>
<link rel="stylesheet" href="https://fonts.googleapis.com/css2?family=Ubuntu:wght@400;500;700&display=swap">
<style>
:root{
  --ink:#ffffff;
  --ink-soft:#dcd8d4;
  --ink-dim:#9a9896;
  --bar:#2a2725;
  --bar-edge:#3a3634;
  --accent:#1e7fd8;
  --night-top:#3a302b;
  --night-mid:#4b4440;
  --night-low:#161414;
  --canvas:#000000;
  --ring:rgba(255,255,255,.28);
  --disc:rgba(0,0,0,.32);
  --field:#232323;
}
*{margin:0;padding:0;box-sizing:border-box}
html,body{width:1200px;height:966px;overflow:hidden;background:var(--canvas)}
body{position:relative;font-family:"Ubuntu",sans-serif;color:var(--ink)}
.hero-photo{position:absolute;left:0;top:0;width:1200px;height:780px;
  background:
    radial-gradient(ellipse 260px 320px at 290px 420px,rgba(190,190,200,.35),transparent 70%),
    radial-gradient(ellipse 200px 300px at 800px 450px,rgba(180,180,190,.3),transparent 70%),
    radial-gradient(ellipse 900px 120px at 600px 640px,rgba(60,110,140,.25),transparent 70%),
    linear-gradient(180deg,var(--night-top) 0%,var(--night-mid) 40%,#2c2826 72%,var(--night-low) 88%,var(--canvas) 100%);}
.site-header{position:absolute;left:0;top:0;width:1200px;height:102px;background:var(--bar);border-bottom:1px solid var(--bar-edge);opacity:.97}
.brand{position:absolute;left:100px;top:66px;display:flex;align-items:center;gap:10px;font-size:26px;font-weight:400;color:var(--ink);letter-spacing:-.3px}
.brand-mark{width:18px;height:18px;background:var(--accent)}
.main-nav{position:absolute;top:38px;left:614px;display:flex;align-items:center;height:28px}
.nav-home{width:32px;height:32px;border-radius:50%;background:#141312;display:flex;align-items:center;justify-content:center;margin-right:16px}
.main-nav a{color:var(--ink-soft);text-decoration:none;font-size:14px;padding:0 21px 0 19px;border-left:1px solid #45403d;line-height:26px}
.welcome{position:absolute;left:393px;top:180px;width:410px;height:410px;border-radius:50%;background:var(--disc);box-shadow:0 0 0 12px rgba(0,0,0,.12)}
.welcome::after{content:"";position:absolute;inset:14px;border:1px solid var(--ring);border-radius:50%}
.welcome-copy{position:absolute;left:0;top:0;width:1200px;text-align:center}
.welcome-title{position:absolute;left:0;width:1196px;top:256px;font-size:26px;font-weight:700;line-height:33px}
.principles{position:absolute;left:0;width:1200px;top:342px;font-size:18px;font-weight:500}
.welcome-text{position:absolute;left:410px;width:376px;top:380px;font-size:14px;line-height:24px;color:var(--ink-soft)}
.divider{position:absolute;left:410px;top:480px;width:378px;height:1px;background:var(--ring)}
.contact-label{position:absolute;left:0;width:1200px;top:490px;font-size:20px}
.contact-icon{position:absolute;left:590px;top:522px}
.contact-phone{position:absolute;left:0;width:1196px;top:542px;font-size:15px}
.social{position:absolute;top:362px;width:56px;height:56px;border-radius:50%;border:1px solid var(--ring);background:rgba(0,0,0,.15)}
.social--left{left:317px}.social--right{left:824px}
.feature{position:absolute;top:675px;width:230px;height:230px;border-radius:50%;background:rgba(20,20,20,.6);text-align:center}
.feature::before{content:"";position:absolute;inset:10px;border:1px solid rgba(255,255,255,.14);border-radius:50%}
.feature-icon{position:absolute;left:0;width:100%;top:26px;display:flex;justify-content:center}
.feature h2{position:absolute;left:0;width:100%;top:76px;font-size:18px;font-weight:500;letter-spacing:.2px}
.feature p{position:absolute;left:18px;width:194px;top:108px;font-size:11px;line-height:16px;color:var(--ink-soft)}
.feature .more{position:absolute;left:0;width:100%;top:170px;font-size:12px;color:var(--ink-soft)}
.feature .more::before{content:"";display:block;margin:0 auto 7px;width:0;height:0;border-left:5px solid transparent;border-right:5px solid transparent;border-top:8px solid var(--ink)}
.signup-field{position:absolute;left:28px;top:114px;width:173px;height:39px;background:var(--field);border:1px solid #2e2e2e;border-radius:2px}
.site-footer{position:absolute;left:0;top:927px;width:1200px;font-size:11px;color:var(--ink-dim)}
.footer-nav{position:absolute;left:111px;display:flex;gap:20px}
.footer-nav a{color:var(--ink-dim);text-decoration:none}
.copyright{position:absolute;right:114px}
</style>
</head>
<body>
<div class="hero-photo" role="img" aria-label="Night photograph of a lit London bridge with towers and the city skyline behind"></div>

<header class="site-header">
  <div class="brand"><span>brightwell capital</span><span class="brand-mark"></span></div>
  <nav class="main-nav">
    <span class="nav-home"><svg width="14" height="12" viewBox="0 0 14 12"><path d="M7 0 0 6h2v6h3.5V8h3v4H12V6h2z" fill="#1e7fd8"/></svg></span>
    <a href="#">About us</a><a href="#">Managed Accounts</a><a href="#">Systems &amp; Performance</a>
  </nav>
</header>

<div class="welcome"></div>
<a class="social social--left" href="#" aria-label="Social profile"></a>
<a class="social social--right" href="#" aria-label="Social profile"></a>

<section class="welcome-copy">
  <h1 class="welcome-title">WELCOME TO<br>BRIGHTWELL CAPITAL</h1>
  <p class="principles">INTEGRITY, INNOVATIVE, PROGRESSIVE</p>
  <p class="welcome-text">Comprar un Remate Hipotecario en VALLE NORTE®, es una excelente forma de inversión de bajo costo y alta utilidad con la garantía de una casa.</p>
  <div class="divider"></div>
  <p class="contact-label">CONTACT</p>
  <svg class="contact-icon" width="16" height="12" viewBox="0 0 16 12"><path d="M1 4C3 0 13 0 15 4l-3 1-1-2H5L4 5zM4 6h8l2 6H2z" fill="#fff"/></svg>
  <p class="contact-phone">(55) 3100 - 4700</p>
</section>

<section class="feature" style="left:101px">
  <div class="feature-icon"><svg width="40" height="40" viewBox="0 0 40 40"><g fill="#fff"><circle cx="20" cy="20" r="13"/><rect x="16" y="1" width="8" height="38" rx="2"/><rect x="16" y="1" width="8" height="38" rx="2" transform="rotate(45 20 20)"/><rect x="16" y="1" width="8" height="38" rx="2" transform="rotate(90 20 20)"/><rect x="16" y="1" width="8" height="38" rx="2" transform="rotate(135 20 20)"/></g><circle cx="20" cy="20" r="6" fill="#141414"/></svg></div>
  <h2>FUND MANAGEMENT</h2>
  <p>Le Lorem Ipsum est simplement<br>du faux texte employé dans la<br>composition et.</p>
  <a class="more">MORE</a>
</section>
<section class="feature" style="left:356px">
  <div class="feature-icon"><svg width="34" height="34" viewBox="0 0 34 34"><path d="M32 2 14 22l-3-3z" fill="#fff"/><path d="M9 20c-4 0-5 4-5 7s-2 4-4 5c6 1 12-1 12-6z" fill="#fff"/></svg></div>
  <h2>ALGORITHMIC DESIGN</h2>
  <p>Le Lorem Ipsum est simplement<br>du faux texte employé dans la<br>composition et.</p>
  <a class="more">MORE</a>
</section>
<section class="feature" style="left:611px">
  <div class="feature-icon"><svg width="32" height="30" viewBox="0 0 32 30"><g fill="#fff"><circle cx="12" cy="9" r="6"/><path d="M0 28c0-8 5-11 12-11s12 3 12 11z"/><circle cx="22" cy="8" r="5"/><path d="M20 15c7 0 12 3 12 11h-6c0-5-2-8-6-11z"/></g></svg></div>
  <h2>TESTIMONIALS</h2>
  <p>Le Lorem Ipsum est simplement<br>du faux texte employé dans la<br>composition et.</p>
  <a class="more">MORE</a>
</section>
<section class="feature" style="left:866px">
  <div class="feature-icon"><svg width="32" height="24" viewBox="0 0 32 24"><rect width="32" height="24" rx="2" fill="#fff"/><path d="M1 2l15 12L31 2" fill="none" stroke="#141414" stroke-width="2"/></svg></div>
  <h2>NEWSLETTER SIGNUP</h2>
  <div class="signup-field" aria-label="Email address"></div>
  <a class="more">SUBMIT</a>
</section>

<footer class="site-footer">
  <nav class="footer-nav"><a href="#">About us</a><a href="#">Managed Accounts</a><a href="#">Systems &amp; Performance</a></nav>
  <p class="copyright">© Copyrights 2013 All rights Reserved</p>
</footer>
</body>
</html>
```